Brent Halvorsen Professional Coaching

I would like a website with a mountain theme geared towards professional executives reaching higher peaks and goals. This is a 3 page website with brand essence information on the opening page, the coaching process on a second page and "about me" and lead capture form on a third page

Target Market(s)

C-Level audience, involved in tech, government, manufacturing, and transportation type of corporations

Coding

Number of Pages Required

3 page

Font styles to use
Sans Serif

Colors
a7a7a7
1b1b1b
e8e8e8
3176b5
abd036
0355a3

Requirements
Must have
• Looking for a user friendly site that I can manage/update going forward. Must have:
• 1. "Is coaching right for you?" - page 1
• 2. "Our Process" page 2 - I will describe how we approach coaching
• 3. "Contact us" page 3 where I can capture contact information from potential clients
• 4. Clean and professional with more modern font
• 5. Links to personal social media sites
• 6. Ability to upload/download .pdf documents as resources
• 7. Ability to add on new pages in the future (such as a blog page)
Nice to have
• I want a place to store articles I write or use.
• LinkedIn or Twitter Feed
Should not have
• Not fluffy or too 'zen' like personal life coaches tend to present.

```html
<!DOCTYPE html>
<html lang="en">
<head>
<meta charset="utf-8">
<title>Brent Halvorsen Professional Coaching</title>
<link rel="stylesheet" href="https://fonts.googleapis.com/css2?family=Montserrat:wght@400;500;600;700&display=swap">
<style>
:root{
  --ink:#1b1b1b;
  --blue:#318bd0;
  --blue-deep:#0355a3;
  --grey:#a7a7a7;
  --paper:#ffffff;
  --footer:#eeeeee;
  --text:#555555;
  --hero-a:#5a5f66;
  --hero-b:#2c2f34;
}
*{margin:0;padding:0;box-sizing:border-box}
html,body{width:1200px;height:2400px;overflow:hidden;background:var(--paper)}
body{font-family:"Montserrat",sans-serif;color:var(--ink);position:relative}
.abs{position:absolute}

/* Hero */
.hero{position:absolute;left:0;top:0;width:1200px;height:700px;
  background:linear-gradient(135deg,#7d838a 0%,var(--hero-a) 40%,var(--hero-b) 100%)}
.topbar{position:absolute;left:0;top:0;width:1200px;height:56px;background:rgba(0,0,0,.82);
  border-bottom:1px solid rgba(255,255,255,.12);color:#fff;font-size:15px;font-weight:500}
.topbar .item{position:absolute;top:18px;display:flex;align-items:center;gap:12px}
.topbar .sep{position:absolute;left:382px;top:19px;width:2px;height:18px;background:#fff}
.social{display:flex;gap:10px}
.social .icon{width:26px;height:26px;border:2px solid currentColor;border-radius:50%;display:flex;align-items:center;justify-content:center}
.social .icon svg{display:block}
.topbar .social{position:absolute;right:115px;top:14px}
.navbar{position:absolute;left:0;top:56px;width:1200px;height:81px;background:rgba(0,0,0,.82);color:#fff}
.brand{position:absolute;left:112px;top:18px;font-size:34px;font-weight:500}
.menu{position:absolute;right:116px;top:32px;display:flex;font-size:16.5px;font-weight:500}
.menu a{color:#fff;text-decoration:none;margin-left:40px}
.hero-copy{position:absolute;left:112px;top:232px;color:#fff}
.hello{font-size:52px;font-weight:600;line-height:64px}
.hello .name{background:var(--blue);padding:0 14px;margin-left:0;display:inline-block;line-height:68px}
.lead{margin-top:18px;font-size:20px;font-weight:500;line-height:31px;width:560px}
.btn-solid{display:inline-block;background:var(--blue);color:#fff;font-weight:600;text-align:center}
.hero .btn-solid{margin-top:18px;width:197px;height:58px;line-height:58px;font-size:20px}
.dots .dot{position:absolute;background:#fff;border-radius:50%}
.edge{position:absolute;left:0;width:1200px}

/* About */
.section-title{font-size:40px;font-weight:700;letter-spacing:.5px}
.title-bar{width:67px;height:5px;background:var(--ink);margin-top:10px}
.about{position:absolute;left:112px;top:836px;width:512px}
.about p{margin-top:26px;font-size:15.5px;line-height:29px;color:var(--text);text-align:justify}
.about .btn-solid{margin-top:30px;width:161px;height:46px;line-height:46px;font-size:17px}
.portrait{position:absolute;left:700px;top:808px}

/* Coaching */
.coaching{position:absolute;left:0;top:1272px;width:1200px;height:740px}
.coaching .head{position:absolute;left:110px;top:124px;color:#fff}
.coaching .title-bar{background:#fff}
.arrows{position:absolute;left:1022px;top:144px;display:flex;gap:9px}
.card{position:absolute;top:235px;width:232px;height:370px;background:#fff}
.card .photo{height:181px}
.card h3{margin:20px 15px 0;font-size:16px;font-weight:600;line-height:24px}
.card p{margin:6px 15px 0;font-size:14px;line-height:22px;color:#777}
.btn-line{position:absolute;left:15px;top:312px;width:122px;height:36px;border:2px solid #555;
  font-size:15px;line-height:32px;text-align:center;color:#444;font-weight:500}

/* Footer */
.footer{position:absolute;left:0;top:2000px;width:1200px;height:400px;background:var(--footer)}
.footer .brand-name{position:absolute;left:134px;top:136px;font-size:31px;font-weight:600;color:var(--blue)}
.footer .social{position:absolute;left:184px;top:192px;color:#333;gap:11px}
.footer .social .icon{width:25px;height:25px;border-width:1.5px}
.col-title{position:absolute;top:76px;font-size:25px;font-weight:500;color:var(--blue)}
.links{position:absolute;left:526px;top:128px;list-style:none;font-size:15px;color:#444}
.links li{height:30px;display:flex;align-items:center;gap:14px}
.links li::before{content:"";border-left:6px solid #666;border-top:5px solid transparent;border-bottom:5px solid transparent}
.contact{position:absolute;left:818px;top:130px;font-size:15px;color:#444;line-height:24px}
.contact .row{display:flex;gap:16px;align-items:flex-start;margin-bottom:10px}
.contact svg{flex:none;margin-top:3px}
.rule{position:absolute;left:112px;top:326px;width:974px;height:2px;background:#bbb}
.legal{position:absolute;top:354px;font-size:14px;color:#555}
.legal-links{right:114px;display:flex;gap:26px}
</style>
</head>
<body>

<header class="hero">
  <div class="topbar">
    <div class="item" style="left:115px">
      <svg width="22" height="16" viewBox="0 0 22 16" fill="none" stroke="#fff" stroke-width="1.8"><rect x="1" y="1" width="20" height="14"/><path d="M1 1l10 8 10-8"/></svg>
      info@brenthalvorsen.com
    </div>
    <div class="sep"></div>
    <div class="item" style="left:404px">
      <svg width="20" height="20" viewBox="0 0 24 24" fill="none" stroke="#fff" stroke-width="1.8"><path d="M5 3h4l2 5-3 2a12 12 0 0 0 6 6l2-3 5 2v4a2 2 0 0 1-2 2A17 17 0 0 1 3 5a2 2 0 0 1 2-2z"/></svg>
      555-014-2286
    </div>
    <div class="social" aria-label="Social media links">
      <span class="icon"><svg width="12" height="12" viewBox="0 0 12 12" fill="none" stroke="currentColor" stroke-width="1.4"><circle cx="6" cy="6" r="5"/><path d="M1 6h10M6 1c2.5 3 2.5 7 0 10M6 1c-2.5 3-2.5 7 0 10"/></svg></span>
      <span class="icon"><svg width="12" height="12" viewBox="0 0 12 12" fill="none" stroke="currentColor" stroke-width="1.4"><path d="M1 2h10v6H5l-3 2.5V8H1z"/></svg></span>
      <span class="icon"><svg width="12" height="12" viewBox="0 0 12 12" fill="none" stroke="currentColor" stroke-width="1.4"><path d="M5 7l2-2M4.5 5L3 6.5a2 2 0 0 0 2.8 2.8L7 8M7.5 7L9 5.5A2 2 0 0 0 6.2 2.7L5 4"/></svg></span>
      <span class="icon"><svg width="12" height="12" viewBox="0 0 12 12" fill="currentColor"><circle cx="3" cy="6" r="1.6"/><circle cx="9" cy="2.5" r="1.6"/><circle cx="9" cy="9.5" r="1.6"/><path d="M3 6L9 2.5M3 6l6 3.5" stroke="currentColor" stroke-width="1"/></svg></span>
    </div>
  </div>
  <nav class="navbar">
    <div class="brand">Brent Halvorsen</div>
    <div class="menu"><a>Home</a><a>About Me</a><a>Coaching Process</a><a>Contact</a></div>
  </nav>
  <div role="img" aria-label="Photo of a coach presenting goals on a flip chart to a seated executive team" class="abs" style="left:0;top:137px;width:1200px;height:563px"></div>
  <div class="hero-copy">
    <div class="hello">Hi,</div>
    <div class="hello">I’m <span class="name">Brent Halvorsen!</span></div>
    <div class="lead">Lorem ipsum dolor sit amet, consectetur adipiscing elit, sed do eiusmod tempor incididunt</div>
    <div class="btn-solid">View More</div>
  </div>
  <div class="dots">
    <div class="dot" style="left:1112px;top:337px;width:22px;height:22px;background:none;border:3px solid #fff"></div>
    <div class="dot" style="left:1117px;top:342px;width:12px;height:12px"></div>
    <div class="dot" style="left:1117px;top:378px;width:13px;height:13px"></div>
    <div class="dot" style="left:1117px;top:405px;width:13px;height:13px"></div>
  </div>
  <svg class="edge" style="top:640px" height="60" viewBox="0 0 1200 60" preserveAspectRatio="none">
    <path fill="#fff" d="M0 22 Q300 4 600 30 T1200 22 L1200 60 L0 60Z"/>
  </svg>
</header>

<section class="about">
  <h2 class="section-title">ABOUT ME</h2>
  <div class="title-bar"></div>
  <p>At vero eos et accusamus et iusto odio dignissimos ducimus qui blanditiis praesentium voluptatum deleniti atque corrupti quos dolores et quas molestias excepturi sint occaecati cupiditate non provident, similique sunt in culpa qui officia deserunt mollitia animi, id est laborum et dolorum fuga. Et harum quidem rerum facilis est et expedita distinctio.</p>
  <div class="btn-solid">Read More</div>
</section>

<svg class="portrait" width="390" height="390" viewBox="0 0 390 390">
  <defs>
    <linearGradient id="portraitTone" x1="0" y1="0" x2="0" y2="1">
      <stop offset="0" stop-color="#5d7a52"/><stop offset="0.55" stop-color="#46596b"/><stop offset="1" stop-color="#2c3a52"/>
    </linearGradient>
  </defs>
  <path d="M188 4 A191 191 0 0 1 188 386" fill="none" stroke="var(--blue)" stroke-width="6"/>
  <path d="M188 4 A191 191 0 0 0 10 150" fill="none" stroke="var(--blue)" stroke-width="3"/>
  <path d="M188 386 A191 191 0 0 1 60 330" fill="none" stroke="var(--blue)" stroke-width="3"/>
  <circle cx="188" cy="192" r="176" fill="url(#portraitTone)" role="img" aria-label="Portrait video of the coach outdoors in a blue blazer"/>
  <circle cx="188" cy="192" r="25" fill="none" stroke="#fff" stroke-width="3.5"/>
  <path d="M181 180 L199 192 181 204Z" fill="#fff"/>
</svg>

<section class="coaching">
  <svg class="edge" style="top:0" height="740" viewBox="0 0 1200 740" preserveAspectRatio="none">
    <path fill="var(--blue)" d="M0 28 Q300 8 600 36 T1200 24 L1200 696 Q900 716 600 700 T0 690Z"/>
  </svg>
  <div class="head">
    <h2 class="section-title">COACHING PROCESS</h2>
    <div class="title-bar"></div>
  </div>
  <div class="arrows">
    <svg width="28" height="28" viewBox="0 0 28 28" fill="none" stroke="#fff" stroke-width="2"><circle cx="14" cy="14" r="12"/><path d="M16 9l-5 5 5 5"/></svg>
    <svg width="28" height="28" viewBox="0 0 28 28" fill="none" stroke="#fff" stroke-width="2"><circle cx="14" cy="14" r="12"/><path d="M12 9l5 5-5 5"/></svg>
  </div>

  <article class="card" style="left:109px">
    <div class="photo" role="img" aria-label="Photo of a coach presenting at a whiteboard to an audience" style="background:linear-gradient(135deg,#6c7884,#2f3a46)"></div>
    <h3>Sed ut perspiciatis unde omnis iste natus</h3>
    <p>Lorem ipsum dolor sit amet, consectetur adipiscing</p>
    <div class="btn-line">Read More</div>
  </article>
  <article class="card" style="left:357px">
    <div class="photo" role="img" aria-label="Photo of a presenter pointing at a board in a sunlit room" style="background:linear-gradient(135deg,#f0d9a8,#8b7a63 60%,#4b4236)"></div>
    <h3>Sed ut perspiciatis unde omnis iste natus</h3>
    <p>Lorem ipsum dolor sit amet, consectetur adipiscing</p>
    <div class="btn-line">Read More</div>
  </article>
  <article class="card" style="left:606px">
    <div class="photo" role="img" aria-label="Photo of a seminar with attendees facing a speaker" style="background:linear-gradient(180deg,#e7eaec,#b9a58c 60%,#3d3f45)"></div>
    <h3>Sed ut perspiciatis unde omnis iste natus</h3>
    <p>Lorem ipsum dolor sit amet, consectetur adipiscing</p>
    <div class="btn-line">Read More</div>
  </article>
  <article class="card" style="left:854px">
    <div class="photo" role="img" aria-label="Photo of a business meeting around a chart in an office with plants" style="background:linear-gradient(135deg,#9fb592,#e2e4e0 50%,#50555c)"></div>
    <h3>Sed ut perspiciatis unde omnis iste natus</h3>
    <p>Lorem ipsum dolor sit amet, consectetur adipiscing</p>
    <div class="btn-line">Read More</div>
  </article>
</section>

<footer class="footer">
  <div class="brand-name">Brent Halvorsen</div>
  <div class="social" aria-label="Social media links">
    <span class="icon"><svg width="11" height="11" viewBox="0 0 12 12" fill="none" stroke="currentColor" stroke-width="1.4"><circle cx="6" cy="6" r="5"/><path d="M1 6h10M6 1c2.5 3 2.5 7 0 10M6 1c-2.5 3-2.5 7 0 10"/></svg></span>
    <span class="icon"><svg width="11" height="11" viewBox="0 0 12 12" fill="none" stroke="currentColor" stroke-width="1.4"><path d="M1 2h10v6H5l-3 2.5V8H1z"/></svg></span>
    <span class="icon"><svg width="11" height="11" viewBox="0 0 12 12" fill="none" stroke="currentColor" stroke-width="1.4"><path d="M5 7l2-2M4.5 5L3 6.5a2 2 0 0 0 2.8 2.8L7 8M7.5 7L9 5.5A2 2 0 0 0 6.2 2.7L5 4"/></svg></span>
    <span class="icon"><svg width="11" height="11" viewBox="0 0 12 12" fill="currentColor"><circle cx="3" cy="6" r="1.6"/><circle cx="9" cy="2.5" r="1.6"/><circle cx="9" cy="9.5" r="1.6"/><path d="M3 6L9 2.5M3 6l6 3.5" stroke="currentColor" stroke-width="1"/></svg></span>
  </div>

  <div class="col-title" style="left:522px">Quick Links</div>
  <ul class="links">
    <li>Home</li><li>About Me</li><li>Coaching</li><li>Process</li><li>Contact</li>
  </ul>

  <div class="col-title" style="left:818px">Contact Us</div>
  <div class="contact">
    <div class="row">
      <svg width="18" height="22" viewBox="0 0 18 22"><path d="M9 0a8 8 0 0 1 8 8c0 6-8 14-8 14S1 14 1 8a8 8 0 0 1 8-8z" fill="var(--blue)"/><circle cx="9" cy="8" r="3" fill="#eee"/></svg>
      <span style="width:240px">72 Ridgeline Street 18/4 Denver<br>City, US</span>
    </div>
    <div class="row">
      <svg width="20" height="20" viewBox="0 0 24 24" fill="none" stroke="var(--blue)" stroke-width="1.8"><path d="M5 3h4l2 5-3 2a12 12 0 0 0 6 6l2-3 5 2v4a2 2 0 0 1-2 2A17 17 0 0 1 3 5a2 2 0 0 1 2-2z"/></svg>
      <span>555 014 -2286</span>
    </div>
    <div class="row">
      <svg width="20" height="15" viewBox="0 0 22 16" fill="none" stroke="var(--blue)" stroke-width="1.8"><rect x="1" y="1" width="20" height="14"/><path d="M1 1l10 8 10-8"/></svg>
      <span>info@brenthalvorsen.com</span>
    </div>
    <div style="margin-top:6px">Open hours: 8.00-18.00 Mon-Fri</div>
  </div>

  <div class="rule"></div>
  <div class="legal" style="left:112px">© Copyrights 2019 | All Rights Reserved</div>
  <div class="legal legal-links"><span>Terms &amp; Conditions</span><span>Privacy Policy</span><span>Contact Us</span></div>
</footer>

</body>
</html>
```